Worksite Kitbag - uFone app for tradespeople - UI design

Worksite Kitbag is an uFone app for tradespeople (builders, carpenters, electricians, etc) which provides a range of tools that will assist with typical tasks, such as the calculation of unit conversion and spatial/volumetric/electrical measurements. The application also makes use of instruments available in the smartphone device to provide useful tools such as a spirit level, compass and torch.

The product is a simple menu-based application consisting of a number of menu and function screens. Each menu item will navigate the user to the function screen applicable to that menu item. Each function screen will contain the necessary inputs and features for perform its stated function.

The user interface should be designed with the tradesperson user in mind and as such should be simple, intuitive and durable with respect to its usability, interface design and branding elements.

Target Market(s)

Tradespeople (builders, carpenters, electricians, etc)

Industry/Entity Type

Trade

Font styles to use
Sans Serif

Requirements
Must have
• Refer to attached wireframes document...
• - Simple design
• - Consistent layout and theme
• - Screens and icons
Should not have
• - Tacky 3D images and textured backgrounds

```html
<!DOCTYPE html>
<html lang="en">
<head>
<meta charset="utf-8">
<title>Worksite Kitbag – Home Menu</title>
<link rel="stylesheet" href="https://fonts.googleapis.com/css2?family=Open+Sans:wght@400;600&display=swap">
<style>
  :root {
    --page-bg: #f3f4f6;
    --screen-bg: #2b2b2c;
    --photo-dark: #262627;
    --photo-mid: #3b3b3c;
    --status-bg: #ffffff;
    --status-ink: #111111;
    --ink-light: #ffffff;
    --button-border: rgba(255, 255, 255, 0.92);
    --button-fill: rgba(0, 0, 0, 0.12);
  }
  * { box-sizing: border-box; margin: 0; padding: 0; }
  html, body {
    width: 1200px; height: 1000px; overflow: hidden;
    background: var(--page-bg);
    font-family: "Open Sans", Arial, sans-serif;
  }
  .app-screen {
    position: absolute; left: 340px; top: 48px;
    width: 520px; height: 904px;
    background: var(--screen-bg);
    overflow: hidden;
  }
  .status-bar {
    position: absolute; left: 0; top: 0; width: 100%; height: 30px;
    background: var(--status-bg); color: var(--status-ink);
    font-size: 17px; display: flex; align-items: center;
    padding: 0 12px; z-index: 2;
  }
  .status-left { display: flex; align-items: center; gap: 6px; flex: 1; }
  .status-time { flex: 1; text-align: center; }
  .status-right { flex: 1; display: flex; justify-content: flex-end; align-items: center; gap: 6px; }
  .hero-photo {
    position: absolute; left: 0; top: 30px; width: 100%; bottom: 0;
    background:
      radial-gradient(ellipse at 72% 45%, var(--photo-mid) 0%, transparent 60%),
      linear-gradient(180deg, var(--photo-dark) 0%, #323233 55%, #2a2a2b 100%);
  }
  .brand {
    position: absolute; left: 0; top: 135px; width: 100%;
    display: flex; flex-direction: column; align-items: center; z-index: 1;
  }
  .brand-mark { width: 96px; height: 76px; background: var(--ink-light); border-radius: 6px; }
  .brand-name {
    margin-top: 22px; color: var(--ink-light);
    font-size: 46px; font-weight: 400; letter-spacing: 1px;
  }
  .main-menu {
    position: absolute; left: 35px; top: 346px; width: 450px; z-index: 1;
    list-style: none;
  }
  .menu-item {
    height: 83px; margin-bottom: 9px;
    border: 2px solid var(--button-border); border-radius: 4px;
    background: var(--button-fill);
    display: flex; align-items: center; justify-content: center;
    color: var(--ink-light); font-size: 19px; font-weight: 600; letter-spacing: 1.2px;
  }
  .contact-link {
    position: absolute; left: 0; top: 827px; width: 100%; text-align: center; z-index: 1;
    color: var(--ink-light); font-size: 19px; font-weight: 600; letter-spacing: 1.2px;
    text-decoration: underline; text-underline-offset: 4px;
  }
</style>
</head>
<body>
  <main class="app-screen">
    <div class="status-bar">
      <div class="status-left">
        <svg width="58" height="12" viewBox="0 0 58 12" aria-hidden="true">
          <circle cx="6" cy="6" r="5" fill="#111"/>
          <circle cx="18" cy="6" r="5" fill="#111"/>
          <circle cx="30" cy="6" r="5" fill="#111"/>
          <circle cx="42" cy="6" r="4.3" fill="none" stroke="#111" stroke-width="1.3"/>
          <circle cx="54" cy="6" r="3.3" fill="none" stroke="#111" stroke-width="1.3"/>
        </svg>
        <span class="carrier">KORA</span>
        <svg width="20" height="15" viewBox="0 0 20 15" aria-hidden="true">
          <path d="M1 5 A13 13 0 0 1 19 5" fill="none" stroke="#111" stroke-width="2.2"/>
          <path d="M4.5 8.5 A8 8 0 0 1 15.5 8.5" fill="none" stroke="#111" stroke-width="2.2"/>
          <path d="M10 14 L7 11 A4 4 0 0 1 13 11 Z" fill="#111"/>
        </svg>
      </div>
      <div class="status-time">11:27 AM</div>
      <div class="status-right">
        <span>100%</span>
        <svg width="38" height="16" viewBox="0 0 38 16" aria-hidden="true">
          <rect x="1" y="1" width="32" height="14" rx="2" fill="none" stroke="#111" stroke-width="1.5"/>
          <rect x="3" y="3" width="28" height="10" fill="#111"/>
          <rect x="34" y="5" width="3" height="6" fill="#111"/>
        </svg>
      </div>
    </div>

    <div class="hero-photo" role="img" aria-label="Dimmed background photo of a tradesperson in glasses using a tablet"></div>

    <header class="brand">
      <div class="brand-mark" aria-hidden="true"></div>
      <h1 class="brand-name">WORKSITE KITBAG</h1>
    </header>

    <ul class="main-menu">
      <li class="menu-item">UNIT CONVERSION</li>
      <li class="menu-item">MEASUREMENT CALCULATION</li>
      <li class="menu-item">SPIRIT LEVEL</li>
      <li class="menu-item">COMPASS</li>
      <li class="menu-item">TORCH</li>
    </ul>

    <a class="contact-link">CONTACT US</a>
  </main>
</body>
</html>
```